Mobile App UI Redesign for Service Booking app

Bookora is a business management system made especially for service based businesses (our subscribers). It enables systemising your service businesses. This can be used by diverse industries like automotive service, beauty (hair salons, nail spas), Spas, Chiropractor, acupuntcure, osteo, yoga studio, business coach, etc.

One component of this management system is a consumer app that the users (customers of our subscribers) can use to book in services with businesses (subscribers). Any business that provides services, either 1-to-1(personal training/ hair cut, etc) or 1-to-many (classes/ sessions)can get their users to download the app and book straight away in real time.

The current app is built as a version that is available to all subscribers. Hence the search screen at the beginning of the app. Our subscribers have the option to brand this app, with their own logo and colours.

The UI of the app needs to be designed using flat and clean UI design trends that are currently prevailing for B2C apps. Even the sliding menu panel can be removed and alternative placement of this functionality can be suggested. The color palette used for the design should be limited (3-5 colours) so that minimum effort is required to convert this into our customers branded app.

The Current UI screens are open to suggestions for change. For ease of booking in minimum steps, consolidation of functionality on different screens can be suggested, accompanies by a rational reason with the objective of having a simple and straight forward user experience.

User should be able to move from one function to another (booking > view appointments > profile) in no more than 1 or max 2 gestures.

Target Market(s)

Service Based Businesses that require customers to book in services or sessions with them. These can include health services (chiro, physio, osteo, accupuncture, etc) Beauty (hair salon, nail spa, health spa, etc) automotive service (car service, motorcycle service, bike service, etc)

Industry/Entity Type

Business

Requirements
Must have
• Design files to be delivered in JPG and Vectored PSD format

```html
<!DOCTYPE html>
<html lang="en">
<head>
<meta charset="utf-8">
<title>Bookora – Business Search</title>
<link rel="stylesheet" href="https://fonts.googleapis.com/css2?family=Open+Sans:wght@400;600&display=swap">
<style>
  :root {
    --brand-blue: #4ba6e6;
    --brand-blue-dark: #3a93d3;
    --field-blue: #6bb8ec;
    --ink: #3b3f44;
    --muted: #8c9096;
    --divider: #e6e8eb;
    --page: #ffffff;
    --tile-black: #0f0f10;
    --tile-navy: #1d2f4a;
    --tile-teal: #1f5f7c;
    --tile-light: #ffffff;
    --tile-border: #cfd8e0;
    --tile-gold: #e3b13b;
    --tile-sky: #8fd3f2;
  }
  * { box-sizing: border-box; margin: 0; padding: 0; }
  html, body { width: 1200px; height: 2352px; overflow: hidden; }
  body {
    background: var(--page);
    font-family: "Open Sans", "Helvetica Neue", Arial, sans-serif;
    color: var(--ink);
  }
  .app-screen { width: 1200px; height: 2352px; display: flex; flex-direction: column; }

  .status-bar {
    height: 62px; background: var(--brand-blue-dark); color: #fff;
    display: flex; align-items: center; justify-content: space-between;
    padding: 0 26px; font-size: 30px; font-weight: 600;
  }
  .status-left, .status-right { display: flex; align-items: center; gap: 12px; width: 300px; }
  .status-right { justify-content: flex-end; }
  .signal { display: flex; gap: 5px; }
  .signal span { width: 13px; height: 13px; border-radius: 50%; background: #fff; }
  .signal span.off { background: transparent; border: 2px solid #fff; }
  .battery { width: 62px; height: 26px; border: 3px solid #fff; border-radius: 5px; padding: 3px; position: relative; }
  .battery::after { content: ""; position: absolute; right: -8px; top: 6px; width: 4px; height: 9px; background: #fff; border-radius: 0 2px 2px 0; }
  .battery i { display: block; height: 100%; background: #fff; border-radius: 2px; }

  .nav-bar {
    height: 118px; background: var(--brand-blue);
    display: flex; align-items: center; padding: 0 30px; gap: 34px;
  }
  .back-button { width: 40px; height: 60px; display: flex; align-items: center; }
  .search-field {
    flex: 1; height: 62px; border-bottom: 3px solid var(--field-blue);
    display: flex; align-items: center; justify-content: space-between;
    padding: 0 6px 0 180px; color: rgba(255,255,255,0.75); font-size: 30px;
  }
  .search-icon {
    width: 54px; height: 54px; border-radius: 50%; background: var(--field-blue);
    display: flex; align-items: center; justify-content: center;
  }

  .business-list { list-style: none; }
  .business-item {
    height: 228px; display: flex; align-items: center; gap: 40px;
    padding: 0 30px 0 30px; border-bottom: 2px solid var(--divider);
  }
  .business-logo {
    width: 258px; height: 180px; flex: none; border-radius: 4px;
    display: flex; align-items: center; justify-content: center; gap: 12px;
    font-size: 30px; font-weight: 600; text-align: center; padding: 0 14px;
  }
  .business-logo .mark { width: 22px; height: 22px; flex: none; }
  .logo-black { background: var(--tile-black); color: var(--tile-gold); }
  .logo-black .mark { background: var(--tile-gold); border-radius: 50%; }
  .logo-light { background: var(--tile-light); color: #6a4a2e; border: 3px solid var(--tile-border); }
  .logo-navy { background: var(--tile-navy); color: var(--tile-gold); }
  .logo-road { background: var(--tile-black); color: var(--tile-gold); }
  .logo-road .mark { background: var(--tile-gold); }
  .logo-teal { background: var(--tile-teal); color: var(--tile-sky); }
  .logo-teal .mark { border: 3px solid var(--tile-sky); border-radius: 50%; }

  .business-info { display: flex; flex-direction: column; gap: 14px; }
  .business-name { font-size: 44px; font-weight: 600; color: var(--ink); margin-bottom: 8px; }
  .business-meta { display: flex; align-items: center; gap: 18px; font-size: 28px; color: var(--muted); }
  .business-meta svg { flex: none; }
</style>
</head>
<body>
<main class="app-screen">
  <div class="status-bar">
    <div class="status-left">
      <div class="signal"><span></span><span></span><span></span><span class="off"></span><span class="off"></span></div>
      <span>DIAL</span>
      <svg width="32" height="24" viewBox="0 0 32 24" aria-hidden="true"><path d="M2 8a20 20 0 0 1 28 0M7 13a13 13 0 0 1 18 0M12 18a6 6 0 0 1 8 0" fill="none" stroke="#fff" stroke-width="3" stroke-linecap="round"/></svg>
    </div>
    <span class="status-time">4:21 PM</span>
    <div class="status-right">
      <svg width="16" height="28" viewBox="0 0 16 28" aria-hidden="true"><path d="M2 8l12 12-6 6V2l6 6L2 20" fill="none" stroke="#fff" stroke-width="2.5" stroke-linejoin="round"/></svg>
      <span>100%</span>
      <div class="battery"><i></i></div>
    </div>
  </div>

  <header class="nav-bar">
    <div class="back-button" aria-label="Back">
      <svg width="24" height="40" viewBox="0 0 24 40"><path d="M20 4L4 20l16 16" fill="none" stroke="#fff" stroke-width="5" stroke-linecap="round" stroke-linejoin="round"/></svg>
    </div>
    <div class="search-field">
      <span>Search for a business</span>
      <span class="search-icon">
        <svg width="26" height="26" viewBox="0 0 26 26" aria-hidden="true"><circle cx="11" cy="11" r="7.5" fill="none" stroke="#fff" stroke-width="3"/><path d="M17 17l6 6" stroke="#fff" stroke-width="3" stroke-linecap="round"/></svg>
      </span>
    </div>
  </header>

  <ul class="business-list">
    <li class="business-item">
      <div class="business-logo logo-black"><span class="mark"></span>Pixel Tailor</div>
      <div class="business-info">
        <h2 class="business-name">Pixel Tailor</h2>
        <p class="business-meta"><svg width="20" height="28" viewBox="0 0 20 28"><path d="M10 27S1 16 1 10a9 9 0 0 1 18 0c0 6-9 17-9 17z" fill="#9a9ea4"/><circle cx="10" cy="10" r="3.5" fill="#fff"/></svg>HARBOURVILLE, 2046, 8 Keel St, Harbourville</p>
        <p class="business-meta"><svg width="22" height="22" viewBox="0 0 24 24"><path d="M6.6 10.8a15 15 0 0 0 6.6 6.6l2.2-2.2a1 1 0 0 1 1-.25 11.4 11.4 0 0 0 3.6.57 1 1 0 0 1 1 1V20a1 1 0 0 1-1 1A17 17 0 0 1 3 4a1 1 0 0 1 1-1h3.5a1 1 0 0 1 1 1c0 1.25.2 2.45.57 3.57a1 1 0 0 1-.25 1z" fill="#9a9ea4"/></svg>555 010 0199</p>
      </div>
    </li>
    <li class="business-item">
      <div class="business-logo logo-light">Bean Summit</div>
      <div class="business-info">
        <h2 class="business-name">Bean Summit</h2>
        <p class="business-meta"><svg width="20" height="28" viewBox="0 0 20 28"><path d="M10 27S1 16 1 10a9 9 0 0 1 18 0c0 6-9 17-9 17z" fill="#9a9ea4"/><circle cx="10" cy="10" r="3.5" fill="#fff"/></svg>HARBOURVILLE, 2046, 8 Keel St, Harbourville</p>
        <p class="business-meta"><svg width="22" height="22" viewBox="0 0 24 24"><path d="M6.6 10.8a15 15 0 0 0 6.6 6.6l2.2-2.2a1 1 0 0 1 1-.25 11.4 11.4 0 0 0 3.6.57 1 1 0 0 1 1 1V20a1 1 0 0 1-1 1A17 17 0 0 1 3 4a1 1 0 0 1 1-1h3.5a1 1 0 0 1 1 1c0 1.25.2 2.45.57 3.57a1 1 0 0 1-.25 1z" fill="#9a9ea4"/></svg>555 010 0199</p>
      </div>
    </li>
    <li class="business-item">
      <div class="business-logo logo-navy">Crest Lane Hospitality</div>
      <div class="business-info">
        <h2 class="business-name">Crest Lane Hospitality</h2>
        <p class="business-meta"><svg width="20" height="28" viewBox="0 0 20 28"><path d="M10 27S1 16 1 10a9 9 0 0 1 18 0c0 6-9 17-9 17z" fill="#9a9ea4"/><circle cx="10" cy="10" r="3.5" fill="#fff"/></svg>HARBOURVILLE, 2046, 8 Keel St, Harbourville</p>
        <p class="business-meta"><svg width="22" height="22" viewBox="0 0 24 24"><path d="M6.6 10.8a15 15 0 0 0 6.6 6.6l2.2-2.2a1 1 0 0 1 1-.25 11.4 11.4 0 0 0 3.6.57 1 1 0 0 1 1 1V20a1 1 0 0 1-1 1A17 17 0 0 1 3 4a1 1 0 0 1 1-1h3.5a1 1 0 0 1 1 1c0 1.25.2 2.45.57 3.57a1 1 0 0 1-.25 1z" fill="#9a9ea4"/></svg>555 010 0199</p>
      </div>
    </li>
    <li class="business-item">
      <div class="business-logo logo-road"><span class="mark"></span>Marvetti Bros</div>
      <div class="business-info">
        <h2 class="business-name">Marvetti Bros</h2>
        <p class="business-meta"><svg width="20" height="28" viewBox="0 0 20 28"><path d="M10 27S1 16 1 10a9 9 0 0 1 18 0c0 6-9 17-9 17z" fill="#9a9ea4"/><circle cx="10" cy="10" r="3.5" fill="#fff"/></svg>HARBOURVILLE, 2046, 8 Keel St, Harbourville</p>
        <p class="business-meta"><svg width="22" height="22" viewBox="0 0 24 24"><path d="M6.6 10.8a15 15 0 0 0 6.6 6.6l2.2-2.2a1 1 0 0 1 1-.25 11.4 11.4 0 0 0 3.6.57 1 1 0 0 1 1 1V20a1 1 0 0 1-1 1A17 17 0 0 1 3 4a1 1 0 0 1 1-1h3.5a1 1 0 0 1 1 1c0 1.25.2 2.45.57 3.57a1 1 0 0 1-.25 1z" fill="#9a9ea4"/></svg>555 010 0199</p>
      </div>
    </li>
    <li class="business-item">
      <div class="business-logo logo-teal"><span class="mark"></span>Pixel Tailor</div>
      <div class="business-info">
        <h2 class="business-name">Pixel Tailor</h2>
        <p class="business-meta"><svg width="20" height="28" viewBox="0 0 20 28"><path d="M10 27S1 16 1 10a9 9 0 0 1 18 0c0 6-9 17-9 17z" fill="#9a9ea4"/><circle cx="10" cy="10" r="3.5" fill="#fff"/></svg>HARBOURVILLE, 2046, 8 Keel St, Harbourville</p>
        <p class="business-meta"><svg width="22" height="22" viewBox="0 0 24 24"><path d="M6.6 10.8a15 15 0 0 0 6.6 6.6l2.2-2.2a1 1 0 0 1 1-.25 11.4 11.4 0 0 0 3.6.57 1 1 0 0 1 1 1V20a1 1 0 0 1-1 1A17 17 0 0 1 3 4a1 1 0 0 1 1-1h3.5a1 1 0 0 1 1 1c0 1.25.2 2.45.57 3.57a1 1 0 0 1-.25 1z" fill="#9a9ea4"/></svg>555 010 0199</p>
      </div>
    </li>
  </ul>
</main>
</body>
</html>
```